New Karvenna Business Cards with new logo

Need to keep the Logo of the guys in the boat, or new logo with guys in a boat that symbolizes the three different Alaska natives that represent the region. Would like to have in font "An Alaska Village Corporation". Business cards should include logo, and be professional. knri.com is the company website that we are looking at redesigning also.

Target Market(s)

Business Contact

Industry/Entity Type

Business

Contact Information for Business Card

Would like Name, title, address, two phone numbers Cell and direct, email.

Logo Text

Logo does not have to have text,

Font styles to use
Serif
Sans Serif

Colors

Designer to choose colors to be used in the design.

Requirements
Must have
• An Alaska Native Village Corporation; Karvenna Heritage Collective Inc. (company name)

```html
<!DOCTYPE html>
<html lang="en">
<head>
<meta charset="utf-8">
<title>Karvenna Business Cards</title>
<link href="https://fonts.googleapis.com/css2?family=Cinzel:wght@500;700&family=Crimson+Text&family=Tenor+Sans&display=swap" rel="stylesheet">
<style>
  :root {
    --stage: #2a2a2c;
    --navy: #2b3a6e;
    --navy-deep: #22305e;
    --gold: #a48b62;
    --sand: #a9916a;
    --sky: #45ade3;
    --meadow: #6cc17a;
    --paper: #ffffff;
    --ink-light: #e9ecf5;
  }
  * { margin: 0; padding: 0; box-sizing: border-box; }
  html, body { width: 1200px; height: 852px; overflow: hidden; background: var(--stage); }
  .canvas { position: relative; width: 1200px; height: 852px; }
  .card {
    position: absolute; width: 560px; height: 320px;
    border-radius: 18px; overflow: hidden; background: var(--paper);
  }
  .card svg.bg { position: absolute; inset: 0; width: 100%; height: 100%; }
  .card-front { left: 30px; top: 266px; }
  .card-back { left: 610px; top: 266px; }

  /* front */
  .brand-mark {
    position: absolute; left: 150px; top: 28px; width: 170px; height: 60px;
    display: flex; align-items: center; justify-content: center; gap: 10px;
    font-family: "Cinzel", serif; font-weight: 700; font-size: 22px;
    color: var(--navy); letter-spacing: 2px;
  }
  .brand-mark .dot { width: 14px; height: 14px; border-radius: 50%; background: var(--gold); }
  .front-heading { position: absolute; left: 60px; top: 100px; width: 350px; text-align: center; }
  .company-line { font-family: "Cinzel", serif; font-weight: 500; font-size: 17px; color: var(--navy); letter-spacing: 0.5px; }
  .person-name { font-family: "Cinzel", serif; font-weight: 700; font-size: 19px; color: var(--navy); margin-top: 6px; }
  .person-title { font-family: "Crimson Text", serif; font-size: 13px; color: var(--gold); }

  .contact { position: absolute; top: 256px; font-family: "Crimson Text", serif; font-size: 13px; color: var(--ink-light); line-height: 1.45; }
  .contact-address { left: 34px; }
  .contact-web { left: 220px; }
  .contact-phone { left: 400px; }
  .contact .row { display: flex; align-items: center; gap: 7px; }
  .contact svg { width: 12px; height: 12px; }
  .divider { position: absolute; top: 258px; width: 1px; height: 34px; background: rgba(255,255,255,0.55); }
  .divider-1 { left: 196px; }
  .divider-2 { left: 378px; }

  /* back */
  .back-mark {
    position: absolute; left: 150px; top: 108px; width: 200px; height: 40px;
    display: flex; align-items: center; justify-content: center; gap: 10px;
    font-family: "Tenor Sans", sans-serif; font-size: 24px; color: var(--navy); letter-spacing: 3px;
  }
  .back-mark .dot { width: 14px; height: 14px; border-radius: 50%; background: var(--paper); }
  .back-text { position: absolute; left: 0; right: 0; top: 244px; text-align: center; font-family: "Tenor Sans", sans-serif; color: var(--paper); }
  .back-company { font-size: 20px; letter-spacing: 1px; }
  .back-web { font-size: 13px; margin-top: 8px; letter-spacing: 0.5px; }
</style>
</head>
<body>
<main class="canvas">

  <section class="card card-front" aria-label="Business card front">
    <svg class="bg" viewBox="0 0 560 320" preserveAspectRatio="none" aria-hidden="true">
      <rect width="560" height="320" fill="var(--paper)"/>
      <path d="M0 214 C140 200 260 190 340 150 C420 108 480 90 560 84 L560 320 L0 320 Z" fill="var(--gold)"/>
      <path d="M0 222 C150 214 270 204 350 162 C430 120 490 102 560 96 L560 320 L0 320 Z" fill="var(--paper)"/>
      <path d="M0 232 C160 226 280 214 360 170 C440 126 495 110 560 104 L560 320 L0 320 Z" fill="var(--navy)"/>
    </svg>
    <div class="brand-mark"><span class="dot"></span>KARVENNA</div>
    <div class="front-heading">
      <p class="company-line">AN ALASKA VILLAGE CORPORATION</p>
      <p class="person-name">DANIEL REYES</p>
      <p class="person-title">Managing Director</p>
    </div>
    <div class="contact contact-address">
      <p>14 Tidewater Lane</p>
      <p>Northbay AK 99603</p>
    </div>
    <span class="divider divider-1"></span>
    <div class="contact contact-web">
      <p class="row">info@knri.com
        <svg viewBox="0 0 12 12" aria-hidden="true"><rect x="0.5" y="2" width="11" height="8" fill="none" stroke="currentColor"/><path d="M0.5 2 L6 6.5 L11.5 2" fill="none" stroke="currentColor"/></svg></p>
      <p class="row">www.knri.com
        <svg viewBox="0 0 12 12" aria-hidden="true"><circle cx="6" cy="6" r="5.3" fill="none" stroke="currentColor"/><ellipse cx="6" cy="6" rx="2.3" ry="5.3" fill="none" stroke="currentColor"/><path d="M0.7 6 H11.3" stroke="currentColor"/></svg></p>
    </div>
    <span class="divider divider-2"></span>
    <div class="contact contact-phone">
      <p class="row">08 5521 0930
        <svg viewBox="0 0 12 12" aria-hidden="true"><path d="M2.5 1 L4.5 1 L5.3 3.6 L4 4.6 C4.7 6 6 7.3 7.4 8 L8.4 6.7 L11 7.5 L11 9.5 C11 10.3 10.3 11 9.5 11 C5 11 1 7 1 2.5 C1 1.7 1.7 1 2.5 1 Z" fill="currentColor"/></svg></p>
      <p class="row">08 5521 0467
        <svg viewBox="0 0 12 12" aria-hidden="true"><rect x="3" y="0.5" width="6" height="11" rx="1" fill="none" stroke="currentColor"/><circle cx="6" cy="9.6" r="0.7" fill="currentColor"/></svg></p>
    </div>
  </section>

  <section class="card card-back" aria-label="Business card back">
    <svg class="bg" viewBox="0 0 560 320" preserveAspectRatio="none" aria-hidden="true">
      <rect width="560" height="320" fill="var(--sky)"/>
      <path d="M0 70 C60 40 110 100 170 75 C240 45 270 10 330 35 C390 60 430 25 470 12 C510 0 540 30 560 24 L560 320 L0 320 Z" fill="var(--paper)"/>
      <path d="M0 86 C60 56 110 116 170 91 C240 61 270 26 330 51 C390 76 430 41 470 28 C510 16 540 46 560 40 L560 320 L0 320 Z" fill="var(--sand)"/>
      <path d="M0 200 C180 176 350 140 560 48 L560 320 L0 320 Z" fill="var(--meadow)"/>
      <path d="M0 214 C180 190 350 154 560 62 L560 320 L0 320 Z" fill="var(--paper)"/>
      <path d="M0 228 C180 204 350 168 560 76 L560 320 L0 320 Z" fill="var(--navy)"/>
      <path d="M0 320 L0 300 C200 280 380 250 560 190 L560 320 Z" fill="var(--navy-deep)" opacity="0.35"/>
    </svg>
    <div class="back-mark"><span class="dot"></span>KARVENNA</div>
    <div class="back-text">
      <p class="back-company">AN ALASKA VILLAGE CORPORATION</p>
      <p class="back-web">www.knri.com</p>
    </div>
  </section>

</main>
</body>
</html>
```